Identity Package (Logo, Website)

We need a logo and website design for a new company.
The new company is a voicemail transcription service provider. It's name is KL9BQZ.io
It will be very transactional. We like the "bootstrap" look and feel, and will be using a developer familiar with bootstrap. Here are the kinds of webpages we like :
https://www.lumenvane.io
http://www.quorbil.com/
http://www.plenivo.com/
There will only be 5 pages, as follows :
1- Homepage
2- Voicemail Transcription for Individuals
3- Voicemail Transcription for Companies
4- Wholesale Voicemail Transcription for Service Providers/Enterprises
5- Contact us
As far as the logo is concerned, we'd like to have just stylized text. It should be done in such a way as to make it easy to see the different elements of the name, which are KL, 2, and BQZ.
Reason: I have received a number of designs, but the designs are mostly from the same few designers (not that much variety in designers). I'd like a few more to compare if possible, so I thought I would keep this open until Monday to give more designers the opportunity to submit over the weekend. Thanks!

```html
<!DOCTYPE html>
<html lang="en">
<head>
<meta charset="utf-8">
<title>KL9BQZ.io — Voicemail Transcription</title>
<link rel="stylesheet" href="https://fonts.googleapis.com/css2?family=Roboto:wght@300;400;700&display=swap">
<style>
:root{
  --blue:#3f95dd;
  --blue-deep:#2f84cc;
  --slate:#454a52;
  --slate-card:#50555e;
  --band-blue:#66798c;
  --band-grey:#7a7a7a;
  --team-grey:#8f8f8f;
  --footer:#3b3b3b;
  --footer-bar:#2b2b2b;
  --white:#ffffff;
  --muted:#6f747c;
  --muted-light:#c9ccd1;
  --list:#7c838e;
}
*{margin:0;padding:0;box-sizing:border-box}
html,body{width:1200px;height:4186px;overflow:hidden}
body{font-family:"Roboto",Helvetica,Arial,sans-serif;font-weight:300;color:var(--white);background:var(--slate)}
section,header,footer{position:relative;width:1200px;overflow:hidden}
.abs{position:absolute}

/* header */
.site-header{height:321px;background:var(--blue)}
.brand{left:112px;top:30px;font-size:34px;font-weight:300;letter-spacing:1px}
.nav{right:112px;top:38px;display:flex;gap:30px;font-size:17px;font-weight:400}
.nav .active{font-weight:700}
.dropdown{left:865px;top:84px;width:106px;height:167px;background:#4aa0e6;border-bottom:4px solid var(--blue-deep);padding:18px 14px;font-size:11px;font-weight:700;line-height:22px}
.dropdown li{list-style:none}
.hero-text{left:112px;top:118px;width:720px;font-size:29px;line-height:40px;color:#e8f3fc}
.hero-link{left:112px;top:220px;font-size:18px;font-weight:400}
.hero-link svg{position:absolute;left:226px;top:2px}

.illustration{height:474px;background:linear-gradient(180deg,#f7a21e 0%,#f08b22 45%,#cfd632 62%,#9cc83a 100%)}

/* intro */
.intro{height:349px;background:var(--slate)}
.intro .lead{left:112px;top:64px;width:930px;font-size:20px;line-height:30px;color:var(--muted-light)}
.intro .col{top:160px;width:460px;font-size:13px;line-height:22px;color:var(--muted)}

/* bands */
.band{height:145px;background:var(--band-blue)}
.band .title{left:112px;top:56px;font-size:30px;font-weight:300;color:#dfe5ea}
.band .title b{font-weight:400;color:var(--white)}
.band .arch{left:112px;top:40px}
.band .plus{right:112px;top:50px}
.band.grey{background:var(--band-grey)}

/* services */
.services{height:427px;background:var(--blue)}
.service{top:62px;width:260px;text-align:center}
.service .ring{width:156px;height:156px;margin:0 auto;border-radius:50%;border:6px solid var(--white);display:flex;align-items:center;justify-content:center}
.service .ring span{width:124px;height:124px;border-radius:50%;background:var(--white);display:flex;align-items:center;justify-content:center}
.service h3{margin-top:40px;font-size:20px;font-weight:400;text-align:left;padding-left:30px}
.service p{margin-top:12px;font-size:12px;line-height:19px;color:#8cc4f0;text-align:left;padding-left:30px;padding-right:20px}

/* pricing */
.pricing{height:712px;background:var(--slate)}
.plan{top:73px;width:307px;height:516px;background:var(--slate-card)}
.plan .head{height:115px;background:var(--white);color:#3d434c;text-align:center;padding-top:26px}
.plan .head h4{font-size:21px;font-weight:300;line-height:28px}
.plan .price{margin-top:6px;display:flex;justify-content:center;align-items:flex-end;height:56px}
.plan .price sup{font-size:30px;align-self:flex-start;margin-top:2px}
.plan .price strong{font-size:60px;font-weight:700;line-height:56px}
.plan .price small{font-size:13px;margin-left:2px;margin-bottom:4px}
.plan ul{list-style:none;text-align:center;padding-top:0}
.plan li{font-size:19px;line-height:44px;color:var(--list)}
.plan .rule{width:60px;height:1px;background:var(--list);margin:84px auto 0}
.plan .cta{text-align:center;margin-top:38px;font-size:22px;font-weight:400;line-height:26px}
.pricing .note{left:230px;top:645px;width:740px;text-align:center;font-size:12px;line-height:20px;color:var(--muted)}

/* team */
.team{height:471px;background:var(--team-grey)}
.member{top:47px;width:307px}
.member .photo{height:229px;background:linear-gradient(180deg,#bdbdbd,#8a8a8a)}
.member .photo.focus{background:linear-gradient(180deg,#f2f2f2,#5c5c5c)}
.member h5{margin-top:28px;font-size:20px;font-weight:400}
.member .role{font-size:11px;color:#e0e0e0}
.member .dots{position:absolute;right:4px;top:262px;display:flex;gap:9px}
.member .dots i{width:9px;height:9px;border-radius:50%;background:#d8d8d8}
.member p{margin-top:12px;font-size:12px;line-height:19px;color:#c4c4c4}

/* contact */
.contact{height:376px;background:linear-gradient(135deg,#a3a3a3,#8e8e8e)}
.contact .address{left:112px;top:34px;font-size:22px;line-height:30px}
.contact .phones{left:112px;top:168px;font-size:22px;line-height:28px;color:#f1f1f1}
.contact .socials{left:112px;top:248px;display:flex;gap:14px}
.contact .socials i{width:40px;height:40px;border-radius:50%;border:2px solid var(--white)}
.field{background:rgba(255,255,255,.18);border:1px solid rgba(255,255,255,.3);font-size:15px;color:#eee;padding:8px 14px}
.contact .send{left:781px;top:194px;font-size:22px;font-weight:400}

/* closing */
.closing{height:324px;background:var(--footer);text-align:center}
.closing .badge{left:555px;top:62px;width:90px;height:90px;border-radius:50%;background:#555}
.closing .quote{left:0;top:190px;width:1200px;font-size:21px;line-height:30px;color:#e6e6e6}
.closing .by{left:0;top:258px;width:1200px;font-size:11px;color:#777}
.bottom-bar{height:62px;background:var(--footer-bar);font-size:11px;color:#6a6a6a}
.bottom-bar .copy{left:112px;top:24px}
.bottom-bar .links{right:112px;top:24px;display:flex;gap:30px}
</style>
</head>
<body>

<header class="site-header">
  <div class="abs brand">KL2BQZ</div>
  <nav class="abs nav"><span>Pages</span><span>News</span><span>Portfolio</span><span class="active">Shortcodes</span><span>Features</span><span>Contact</span></nav>
  <ul class="abs dropdown"><li>Accordion</li><li>Price Table</li><li>Tabs</li><li>Icons</li><li>Tables</li><li>Buttons</li></ul>
  <p class="abs hero-text">This is an important port of call in the Pacific, where all the mail-steamers, and those carrying travellers</p>
  <div class="abs hero-link">Learn More About
    <svg width="10" height="20" viewBox="0 0 10 20"><path d="M2 2 L8 10 L2 18" fill="none" stroke="#fff" stroke-width="3"/></svg>
  </div>
</header>

<section class="illustration" role="img" aria-label="Flat illustration of a city park at sunset with street lamps, trees, people walking and a circuit-line sky"></section>

<section class="intro">
  <p class="abs lead">At dawn on the 13th the Carnatic entered the port of Yokohama.&nbsp; This is an important port of call in the Pacific, where all the mail-steamers, and those carrying travellers</p>
  <p class="abs col" style="left:112px">The river town wakes slowly, and the harbour fills with boats from every coast. Traders line the quay with crates of tea, silk and lacquer, while travellers wait for word of the next steamer bound for the open sea beyond the bay.</p>
  <p class="abs col" style="left:586px">Our traveller walked the wide streets without a plan, taking each turn as it came. He passed bright shop fronts, busy stalls and quiet gardens, and found the town more lively than any he had seen on the long voyage west.</p>
</section>

<section class="band">
  <svg class="abs arch" width="40" height="14" viewBox="0 0 40 14"><path d="M3 12 Q20 -2 37 12" fill="none" stroke="#fff" stroke-width="4" stroke-linecap="round"/></svg>
  <h2 class="abs title">A few words <b>About Us</b></h2>
  <svg class="abs plus" width="46" height="46" viewBox="0 0 46 46"><circle cx="23" cy="23" r="21" fill="none" stroke="#fff" stroke-width="3"/><path d="M23 13v20M13 23h20" stroke="#fff" stroke-width="4"/></svg>
</section>

<section class="services">
  <div class="abs service" style="left:79px">
    <div class="ring"><span><svg width="56" height="56" viewBox="0 0 56 56"><g fill="#3f95dd"><circle cx="28" cy="28" r="17"/><rect x="24" y="4" width="8" height="48"/><rect x="4" y="24" width="48" height="8"/><rect x="24" y="4" width="8" height="48" transform="rotate(45 28 28)"/><rect x="24" y="4" width="8" height="48" transform="rotate(-45 28 28)"/></g><circle cx="28" cy="28" r="7" fill="#fff"/></svg></span></div>
    <h3>Service 2</h3>
    <p>Every message you miss is turned into clear text and sent to you within minutes.</p>
  </div>
  <div class="abs service" style="left:344px">
    <div class="ring"><span><svg width="40" height="60" viewBox="0 0 40 60"><rect x="3" y="3" width="34" height="54" rx="6" fill="none" stroke="#3f95dd" stroke-width="5"/><rect x="9" y="11" width="22" height="32" fill="#3f95dd"/><circle cx="20" cy="50" r="3" fill="#3f95dd"/></svg></span></div>
    <h3>Service 1</h3>
    <p>Read your voicemail on any phone, tablet or desktop, wherever you happen to be.</p>
  </div>
  <div class="abs service" style="left:604px">
    <div class="ring"><span><svg width="60" height="60" viewBox="0 0 60 60"><path d="M52 6 L24 38 L20 34 Z" fill="#3f95dd"/><path d="M8 54 Q10 40 20 38 L24 42 Q22 52 8 54 Z" fill="#3f95dd"/></svg></span></div>
    <h3>Service 3</h3>
    <p>Simple setup that works with the number you already have, with no new hardware.</p>
  </div>
  <div class="abs service" style="left:860px">
    <div class="ring"><span><svg width="62" height="52" viewBox="0 0 62 52"><rect x="21" y="3" width="20" height="10" rx="2" fill="none" stroke="#3f95dd" stroke-width="4"/><rect x="3" y="12" width="56" height="38" rx="4" fill="#3f95dd"/><rect x="3" y="28" width="56" height="3" fill="#fff"/><rect x="27" y="25" width="8" height="9" fill="#fff"/></svg></span></div>
    <h3>Service 4</h3>
    <p>Flexible volume pricing and tools for teams, offices and service providers.</p>
  </div>
</section>

<section class="band">
  <svg class="abs arch" width="40" height="14" viewBox="0 0 40 14"><path d="M3 12 Q20 -2 37 12" fill="none" stroke="#fff" stroke-width="4" stroke-linecap="round"/></svg>
  <h2 class="abs title">Our key <b>Services</b></h2>
  <svg class="abs plus" width="46" height="46" viewBox="0 0 46 46"><circle cx="23" cy="23" r="21" fill="#3f95dd" stroke="#fff" stroke-width="3"/><path d="M23 13v20M13 23h20" stroke="#fff" stroke-width="4"/></svg>
</section>

<section class="pricing">
  <div class="abs plan" style="left:112px">
    <div class="head"><h4>Individuals</h4><div class="price"><sup>$</sup><strong>0</strong><small>/month</small></div></div>
    <ul><li>Vestibulum est</li><li>Accumsan posuere</li><li>Sodales molestie</li><li>Mauris ut ante lacus</li><li>Vehicula dignissim</li></ul>
    <div class="rule"></div>
    <div class="cta">Sign Up Now <svg width="10" height="20" viewBox="0 0 10 20"><path d="M2 2 L8 10 L2 18" fill="none" stroke="#fff" stroke-width="3"/></svg></div>
  </div>
  <div class="abs plan" style="left:446px">
    <div class="head"><h4>Companies</h4><div class="price"><sup>$</sup><strong>10</strong><small>/month</small></div></div>
    <ul><li>Vestibulum est</li><li>Accumsan posuere</li><li>Sodales molestie</li><li>Mauris ut ante lacus</li><li>Vehicula dignissim</li></ul>
    <div class="rule"></div>
    <div class="cta">Sign Up Now <svg width="10" height="20" viewBox="0 0 10 20"><path d="M2 2 L8 10 L2 18" fill="none" stroke="#fff" stroke-width="3"/></svg></div>
  </div>
  <div class="abs plan" style="left:781px">
    <div class="head"><h4>Enterprises</h4><div class="price"><sup>$</sup><strong>20</strong><small>/month</small></div></div>
    <ul><li>Vestibulum est</li><li>Accumsan posuere</li><li>Sodales molestie</li><li>Mauris ut ante lacus</li><li>Vehicula dignissim</li></ul>
    <div class="rule"></div>
    <div class="cta">Sign Up Now <svg width="10" height="20" viewBox="0 0 10 20"><path d="M2 2 L8 10 L2 18" fill="none" stroke="#fff" stroke-width="3"/></svg></div>
  </div>
  <p class="abs note">Plans can be changed at any time from your account page. Prices are shown per month and include all standard features; larger volumes and custom terms are available for service providers on request.</p>
</section>

<section class="band grey">
  <svg class="abs arch" width="40" height="14" viewBox="0 0 40 14"><path d="M3 12 Q20 -2 37 12" fill="none" stroke="#fff" stroke-width="4" stroke-linecap="round"/></svg>
  <h2 class="abs title">Let's talk about <b>Price</b></h2>
  <svg class="abs plus" width="46" height="46" viewBox="0 0 46 46"><circle cx="23" cy="23" r="21" fill="none" stroke="#fff" stroke-width="3"/><path d="M23 13v20M13 23h20" stroke="#fff" stroke-width="4"/></svg>
</section>

<section class="team">
  <div class="abs member" style="left:112px">
    <div class="photo" role="img" aria-label="Portrait photo of Nadia Holloway"></div>
    <div class="dots"><i></i><i></i><i></i></div>
    <h5>Nadia Holloway</h5><div class="role">Founder, CEO</div>
    <p>She leads the team and the plan, keeping the service simple, fast and clear for every customer who calls in each day.</p>
  </div>
  <div class="abs member" style="left:446px">
    <div class="photo focus" role="img" aria-label="Portrait photo of Mira T. Okafor"></div>
    <div class="dots"><i></i><i></i><i></i></div>
    <h5>Mira T. Okafor</h5><div class="role">Founder, Art Director</div>
    <p>She shapes how the product looks and feels, from the first screen to the last message that lands in your inbox.</p>
  </div>
  <div class="abs member" style="left:781px">
    <div class="photo" role="img" aria-label="Portrait photo of Lena Castillo"></div>
    <div class="dots"><i></i><i></i><i></i></div>
    <h5>Lena Castillo</h5><div class="role">Web Designer</div>
    <p>She builds the pages you use every day, making sure each one loads quickly and reads well on any screen size.</p>
  </div>
</section>

<section class="band grey" style="background:#6f6f6f">
  <svg class="abs arch" width="40" height="14" viewBox="0 0 40 14"><path d="M3 12 Q20 -2 37 12" fill="none" stroke="#fff" stroke-width="4" stroke-linecap="round"/></svg>
  <h2 class="abs title">The greatest <b>Team</b></h2>
  <svg class="abs plus" width="46" height="46" viewBox="0 0 46 46"><circle cx="23" cy="23" r="21" fill="none" stroke="#fff" stroke-width="3"/><path d="M23 13v20M13 23h20" stroke="#fff" stroke-width="4"/></svg>
</section>

<section class="contact" role="img" aria-label="Muted street map of the office neighbourhood behind the contact form">
  <div class="abs address">482 Halvern Street<br>Dover, DE 19904</div>
  <div class="abs phones">Phone: 555-014-2290<br>Fax: 555-014-2291</div>
  <div class="abs socials"><i></i><i></i><i></i></div>
  <div class="abs field" style="left:446px;top:81px;width:307px;height:175px">Message</div>
  <div class="abs field" style="left:781px;top:86px;width:307px;height:31px;padding-top:5px">Name</div>
  <div class="abs field" style="left:781px;top:136px;width:307px;height:31px;padding-top:5px">E-mail</div>
  <div class="abs send">Send Message <svg width="10" height="20" viewBox="0 0 10 20"><path d="M2 2 L8 10 L2 18" fill="none" stroke="#fff" stroke-width="3"/></svg></div>
</section>

<section class="band grey" style="background:#717171">
  <svg class="abs arch" width="40" height="14" viewBox="0 0 40 14"><path d="M3 12 Q20 -2 37 12" fill="none" stroke="#fff" stroke-width="4" stroke-linecap="round"/></svg>
  <h2 class="abs title">How to <b>Contact Us</b></h2>
  <svg class="abs plus" width="46" height="46" viewBox="0 0 46 46"><circle cx="23" cy="23" r="21" fill="none" stroke="#fff" stroke-width="3"/><path d="M23 13v20M13 23h20" stroke="#fff" stroke-width="4"/></svg>
</section>

<section class="closing">
  <div class="abs badge"></div>
  <p class="abs quote">He had nothing better to do than, taking chance for his<br>guide, to wander aimlessly through the streets of Yokohama.</p>
  <p class="abs by">— a traveller</p>
</section>

<footer class="bottom-bar">
  <div class="abs copy">© 2014 KL9BQZ.io. All rights reserved.</div>
  <div class="abs links"><span>BLOG</span><span>TERMS</span><span>PRIVACY</span></div>
</footer>

</body>
</html>
```